Letterhead

Can you please design me a letterhead that I can use electronically in word as a template. I have attached my business card as I would like the design to reflect this logo.

```html
<!DOCTYPE html>
<html lang="en">
<head>
<meta charset="utf-8">
<title>Kestrel Business Consultants – Letterhead</title>
<link rel="stylesheet" href="https://fonts.googleapis.com/css2?family=Arimo:wght@400;700&family=Open+Sans:wght@400;600&display=swap">
<style>
  :root {
    --brand-red: #c0272d;
    --band-red: #b52025;
    --ink: #111111;
    --text-grey: #3a3a3a;
    --paper: #ffffff;
    --backdrop: #f1f1f1;
  }
  * { margin: 0; padding: 0; box-sizing: border-box; }
  html, body {
    width: 1200px;
    height: 900px;
    overflow: hidden;
    background: var(--backdrop);
  }
  .letterhead {
    position: absolute;
    left: 324px;
    top: 61px;
    width: 551px;
    height: 779px;
    background: var(--paper);
  }
  .brand {
    position: absolute;
    left: 25px;
    top: 20px;
  }
  .brand-name {
    font-family: "Arimo", Arial, sans-serif;
    font-weight: 400;
    font-size: 46px;
    line-height: 46px;
    letter-spacing: -0.5px;
    color: var(--brand-red);
  }
  .brand-tagline {
    margin-top: 2px;
    margin-left: 3px;
    font-family: "Arimo", Arial, sans-serif;
    font-size: 10px;
    color: var(--ink);
    letter-spacing: 0.1px;
  }
  .contact {
    position: absolute;
    right: 26px;
    top: 34px;
    text-align: right;
    font-family: "Open Sans", Arial, sans-serif;
    font-size: 7px;
    line-height: 8px;
    color: var(--text-grey);
  }
  .contact-name {
    font-weight: 600;
    font-size: 8px;
    line-height: 9px;
    color: var(--text-grey);
  }
  .contact-role {
    color: var(--brand-red);
    margin-bottom: 4px;
  }
  .contact-label {
    color: var(--brand-red);
    font-weight: 600;
  }
  .footer-band {
    position: absolute;
    left: 0;
    bottom: 0;
    width: 100%;
    height: 13px;
    display: flex;
  }
  .footer-band-red { flex: 0 0 474px; background: var(--band-red); }
  .footer-band-black { flex: 1; background: var(--ink); }
</style>
</head>
<body>
  <main class="letterhead">
    <header class="brand">
      <div class="brand-name">kestrel</div>
      <div class="brand-tagline">Business Consultants Pty Ltd</div>
    </header>
    <address class="contact" style="font-style:normal">
      <div class="contact-name">Miriam Calloway</div>
      <div class="contact-role">Principal</div>
      <div><span class="contact-label">P</span> : 0400 555 018</div>
      <div><span class="contact-label">E</span> : miriam@kestrelgroup.net.au</div>
      <div><span class="contact-label">ACN</span> : 012 345 678</div>
    </address>
    <footer class="footer-band">
      <div class="footer-band-red"></div>
      <div class="footer-band-black"></div>
    </footer>
  </main>
</body>
</html>
```